Lanterne architecture business cards

We are a new company based in New Zealand. We Specialize in High end Luxury Residential Architecture.

Every home is bespoke and is designed to each clients individual requirements and needs.

I like to design buildings that inspire people through light and form while offering a high level of comfort and usability.

Lines of sight, proportion and balance are fundamental to the spaces I create.
Updates

August 5th is current deadline - Today's date is the 13th of August.

Target Market(s)

New Zealanders who want a custom individual home design, typically 30-65 year old males and females

Industry/Entity Type

Architecture

Contact Information for Business Card

Director - Derek Tolson
Contact Number - 0279164073
Email - info@lanternearchitecture-example.co.nz
Webstie - www.lanternearchitecture-example.co.nz
Social Media - @lanternearchitecture

Font styles to use
Sans Serif

Requirements
Must have
• Logo (Both Sides)
Website
Email
Contact Number
Social Media

Nice to have
• Texture
Should not have
• More than 3 colours - typically I would've thought 2 would be good to match the logo.

```html
<!DOCTYPE html>
<html lang="en">
<head>
<meta charset="utf-8">
<title>Lanterne Architecture – Business Cards</title>
<link rel="stylesheet" href="https://fonts.googleapis.com/css2?family=Quicksand:wght@400;500;700&display=swap">
<style>
  :root {
    --stage: #2b2b2b;
    --card: #0b0b0b;
    --ink: #f2f2f2;
    --muted: #bdbdbd;
    --silver-light: #f4f4f4;
    --silver-mid: #a9a9a9;
    --silver-dark: #5e5e5e;
  }
  * { box-sizing: border-box; margin: 0; padding: 0; }
  html, body { width: 1200px; height: 900px; overflow: hidden; }
  body {
    background: var(--stage);
    font-family: "Quicksand", sans-serif;
    color: var(--ink);
    position: relative;
  }
  .card {
    position: absolute;
    left: 280px;
    width: 640px;
    height: 366px;
    background: var(--card);
    border-radius: 34px;
    overflow: hidden;
    box-shadow: 0 14px 30px rgba(0,0,0,0.45);
  }
  .card--back { top: 48px; }
  .card--front { top: 486px; }
  .card__band { position: absolute; inset: 0; width: 100%; height: 100%; }

  .brand-name {
    position: absolute; left: 0; right: 0;
    text-align: center;
    color: var(--ink);
    font-weight: 500;
    line-height: 1;
    white-space: nowrap;
  }
  .card--back .brand-name { top: 196px; font-size: 36px; letter-spacing: 1px; }
  .card--back .rule {
    position: absolute; left: 110px; right: 110px; top: 252px;
    height: 1px; background: var(--muted);
  }
  .card--back .handle {
    position: absolute; left: 0; right: 0; top: 272px;
    text-align: center; font-size: 22px; letter-spacing: 1.5px; font-weight: 500;
  }

  .card--front .brand-name { top: 168px; font-size: 28px; letter-spacing: 1px; }

  .holder {
    position: absolute; left: 34px; top: 268px;
    font-size: 26px; font-weight: 700; letter-spacing: 0.5px; text-transform: uppercase;
    white-space: nowrap;
  }
  .divider {
    position: absolute; left: 262px; top: 236px; width: 1px; height: 92px; background: var(--muted);
  }
  .contact {
    position: absolute; left: 278px; top: 238px; list-style: none;
    font-size: 15px; font-weight: 500; line-height: 30px;
  }
  .contact li { display: flex; align-items: center; gap: 9px; white-space: nowrap; }
  .contact svg { width: 15px; height: 15px; flex: none; }
</style>
</head>
<body>

<section class="card card--back" aria-label="Card back">
  <svg class="card__band" viewBox="0 0 640 366" preserveAspectRatio="none" aria-hidden="true">
    <defs>
      <linearGradient id="silverBack" x1="0" y1="0" x2="1" y2="0.3">
        <stop offset="0" stop-color="#5e5e5e"/>
        <stop offset="0.22" stop-color="#f4f4f4"/>
        <stop offset="0.5" stop-color="#a9a9a9"/>
        <stop offset="0.75" stop-color="#f4f4f4"/>
        <stop offset="1" stop-color="#5e5e5e"/>
      </linearGradient>
    </defs>
    <path d="M0 0 H640 V58 C470 64 240 92 0 178 Z" fill="url(#silverBack)"/>
    <path d="M0 178 C240 92 470 64 640 58" fill="none" stroke="#f4f4f4" stroke-width="3"/>
    <path d="M0 186 C240 100 470 72 640 66" fill="none" stroke="#000" stroke-opacity="0.6" stroke-width="8"/>
  </svg>
  <p class="brand-name">Lanterne Architecture</p>
  <div class="rule"></div>
  <p class="handle">@lanternearchitecture</p>
</section>

<section class="card card--front" aria-label="Card front">
  <svg class="card__band" viewBox="0 0 640 366" preserveAspectRatio="none" aria-hidden="true">
    <defs>
      <linearGradient id="silverFront" x1="0" y1="0" x2="1" y2="0.3">
        <stop offset="0" stop-color="#5e5e5e"/>
        <stop offset="0.2" stop-color="#f4f4f4"/>
        <stop offset="0.48" stop-color="#a9a9a9"/>
        <stop offset="0.72" stop-color="#f4f4f4"/>
        <stop offset="1" stop-color="#5e5e5e"/>
      </linearGradient>
    </defs>
    <path d="M0 0 H640 V48 C460 54 240 80 0 150 Z" fill="url(#silverFront)"/>
    <path d="M0 150 C240 80 460 54 640 48" fill="none" stroke="#f4f4f4" stroke-width="3"/>
    <path d="M0 158 C240 88 460 62 640 56" fill="none" stroke="#000" stroke-opacity="0.6" stroke-width="8"/>
  </svg>
  <p class="brand-name">Lanterne Architecture</p>
  <p class="holder">Derek Tolson</p>
  <div class="divider"></div>
  <ul class="contact">
    <li>
      <svg viewBox="0 0 16 16" aria-hidden="true"><rect x="4" y="1" width="8" height="14" rx="1.5" fill="none" stroke="currentColor" stroke-width="1.4"/><circle cx="8" cy="12.5" r="0.9" fill="currentColor"/></svg>
      0279164073
    </li>
    <li>
      <svg viewBox="0 0 16 16" aria-hidden="true"><rect x="1.5" y="3.5" width="13" height="9" rx="1" fill="none" stroke="currentColor" stroke-width="1.4"/><path d="M1.5 4 L8 9 L14.5 4" fill="none" stroke="currentColor" stroke-width="1.4"/></svg>
      info@lanternearchitecture-example.co.nz
    </li>
    <li>
      <svg viewBox="0 0 16 16" aria-hidden="true"><circle cx="8" cy="8" r="6.3" fill="none" stroke="currentColor" stroke-width="1.4"/><ellipse cx="8" cy="8" rx="2.8" ry="6.3" fill="none" stroke="currentColor" stroke-width="1.2"/><path d="M1.7 8 H14.3" stroke="currentColor" stroke-width="1.2"/></svg>
      www.lanternearchitecture-example.co.nz
    </li>
  </ul>
</section>

</body>
</html>
```